Interior Design business card design

I am an interior decorator - dont want to specify decorating more just design.
Want organic looking logo - charcoal and white - with touch of lime green.
Like the idea of some sort of spiral in corner but writing in a line
want lower case, tildamarchetti as one and designs in different font underneath. Maybe using t and m as logo.
More modern than traditional. My clients are mid to top end residential

Target Market(s)

medium to top end homeowners

Industry/Entity Type

Residential

Contact Information for Business Card

Tilda Marchetti Designs
58 Kellaway ave
Pemberly 2190 NSW
Tel 0417268914
tildamarchetti@velnaro.com.au

Logo Text

Tilda Marchetti Designs

Logo styles of interest
Abstract Logo
Lettermark Logo
Requirements
Must have
• Name address ph and e mail
Nice to have
• Contemporary
smart but organic
Should not have
• no traditional fonts

```html
<!DOCTYPE html>
<html lang="en">
<head>
<meta charset="utf-8">
<title>tildamarchetti – business card</title>
<link rel="stylesheet" href="https://fonts.googleapis.com/css2?family=Didact+Gothic&display=swap">
<style>
  :root {
    --backdrop: #b8c6bf;
    --card-white: #ffffff;
    --charcoal: #403848;
    --ink: #2b2631;
    --lime: #8ee533;
    --lime-soft: #a8ec62;
  }
  * { margin: 0; padding: 0; box-sizing: border-box; }
  html, body {
    width: 1200px;
    height: 1167px;
    overflow: hidden;
    background: var(--backdrop);
  }
  .canvas {
    position: relative;
    width: 1200px;
    height: 1167px;
    font-family: "Didact Gothic", "Helvetica Neue", Arial, sans-serif;
    color: var(--ink);
  }
  .card-front {
    position: absolute;
    left: 44px;
    top: 0;
    width: 1087px;
    height: 610px;
    background: var(--card-white);
    overflow: hidden;
  }
  .pattern-field {
    position: absolute;
    left: 0;
    top: 0;
    width: 1087px;
    height: 610px;
  }
  .front-details {
    position: absolute;
    left: 620px;
    top: 78px;
    width: 440px;
    text-align: center;
  }
  .wordmark {
    font-size: 52px;
    letter-spacing: 1px;
    line-height: 1;
    color: var(--ink);
  }
  .monogram-small {
    margin-top: 26px;
    font-size: 104px;
    line-height: 1;
    color: var(--lime);
  }
  .address {
    margin-top: 34px;
    font-size: 29px;
    line-height: 38px;
  }
  .contact {
    margin-top: 30px;
    font-size: 24px;
    line-height: 36px;
  }
  .card-back {
    position: absolute;
    left: 44px;
    top: 610px;
    width: 1087px;
    height: 557px;
    background: var(--charcoal);
    display: flex;
    align-items: center;
    justify-content: center;
  }
  .monogram-large {
    font-size: 230px;
    line-height: 1;
    color: var(--lime);
    margin-top: -12px;
  }
</style>
</head>
<body>
<main class="canvas">
  <section class="card-front">
    <svg class="pattern-field" viewBox="0 0 1087 610" role="img" aria-label="Decorative field of charcoal and lime green dots on white, with a curved right edge">
      <defs>
        <linearGradient id="dotTone" x1="0" y1="0" x2="1" y2="1">
          <stop offset="0" stop-color="#6b6470"/>
          <stop offset="0.5" stop-color="#5f7a4e"/>
          <stop offset="1" stop-color="#6b6470"/>
        </linearGradient>
      </defs>
      <path d="M0 0 H601 C540 70 515 160 528 250 C542 360 610 480 686 610 H0 Z" fill="url(#dotTone)"/>
    </svg>
    <div class="front-details">
      <h1 class="wordmark">tildamarchetti</h1>
      <div class="monogram-small">TM</div>
      <p class="address">Tilda Marchetti<br>Kellaway ave Pemberly<br>2190 NSW</p>
      <p class="contact">tel. 0417268914<br>e: tildamarchetti@velnaro.com.au</p>
    </div>
  </section>
  <section class="card-back">
    <div class="monogram-large">TM</div>
  </section>
</main>
</body>
</html>
```